Need logo and design for business card "BrookVale Plumbing Services".

Needing a design for plumbing company 'BrookVale Plumbing Services', a company based on the surfcoast.
Would like the colour black and blue incorporated. We offer free quotes and reliable friendly service, but don't want this writing on front of card.

I do not have a logo so wanting ideas. Any logo ideas on it would be great.

Target Market(s)

People wanting a Plumber

Industry/Entity Type

Business

Requirements
Must have
• Domestic Plumbing
• Commercial Plumbing
• Roofing
• Gasfitting
Nice to have
• Maybe some sort of plumbing picture on it, spanner, toilet, tap with water etc. Just relating to plumbing.
• BrookVale is on word also with the capital A in it.

```html
<!DOCTYPE html>
<html lang="en">
<head>
<meta charset="utf-8">
<title>BrookVale Plumbing Services – Business Card</title>
<link rel="stylesheet" href="https://fonts.googleapis.com/css2?family=Oswald:wght@400;500&display=swap">
<style>
  :root {
    --brand-blue: #0a72b8;
    --band-grey: #e4e4e2;
    --ink: #141414;
  }
  html, body {
    margin: 0;
    padding: 0;
    width: 1200px;
    height: 686px;
    overflow: hidden;
    background: var(--brand-blue);
  }
  .card {
    position: relative;
    width: 1200px;
    height: 686px;
    background: var(--brand-blue);
    font-family: "Oswald", "Arial Narrow", sans-serif;
  }
  .pattern-field {
    position: absolute;
    left: 0;
    width: 1200px;
    height: 183px;
    background: linear-gradient(180deg, #0b74bb 0%, #096ab0 100%);
  }
  .pattern-field--top { top: 0; }
  .pattern-field--bottom { bottom: 0; }
  .name-band {
    position: absolute;
    top: 183px;
    left: 0;
    width: 1200px;
    height: 320px;
    background: var(--band-grey);
  }
  .brand {
    position: absolute;
    top: 42px;
    left: 0;
    width: 1200px;
    display: flex;
    justify-content: center;
    align-items: center;
    gap: 26px;
  }
  .brand__dot {
    width: 70px;
    height: 70px;
    border-radius: 50%;
    background: var(--brand-blue);
    flex: none;
  }
  .brand__name {
    color: var(--ink);
    font-weight: 500;
    text-transform: uppercase;
    line-height: 1;
  }
  .brand__main {
    display: block;
    font-size: 66px;
    letter-spacing: 2px;
  }
  .brand__sub {
    display: block;
    margin-top: 8px;
    font-size: 40px;
    letter-spacing: 2px;
  }
  .services {
    position: absolute;
    top: 238px;
    left: 0;
    width: 1200px;
    margin: 0;
    text-align: center;
    font-size: 29px;
    font-weight: 500;
    letter-spacing: 1.6px;
    color: var(--ink);
    text-transform: uppercase;
  }
  .services__sep {
    color: var(--brand-blue);
    margin: 0 8px;
  }
</style>
</head>
<body>
  <div class="card">
    <div class="pattern-field pattern-field--top" role="img" aria-label="Decorative white wave lattice pattern on blue"></div>

    <section class="name-band">
      <div class="brand">
        <span class="brand__dot"></span>
        <h1 class="brand__name" style="margin:0">
          <span class="brand__main">BrookVale</span>
          <span class="brand__sub">Plumbing Services</span>
        </h1>
      </div>
      <p class="services">
        Domestic Plumbing<span class="services__sep">-</span>Commercial Plumbing<span class="services__sep">-</span>Roofing<span class="services__sep">-</span>Gasfitting
      </p>
    </section>

    <div class="pattern-field pattern-field--bottom" role="img" aria-label="Decorative white wave lattice pattern on blue"></div>
  </div>
</body>
</html>
```